Kleine Website f. Unternehmensdarstellung
Zielgruppe
Geschäftsführer, Marketing & Sales Manager asiatischer Konzerne.
Aufgabenstellung
Wir sind eine Consulting und Handelsagentur mit überwiegend internationaler Kundschaft (Asien 70%).
Für einen Webauftritt, ca. 8 Seiten, haben wir eine Powerpoint Vorlage erstellt, diese zeigt nur die Inhalte. Wir benötigen nun daraus eine Website, haben eigenen Webspace, eigener Server bei Servantik. Wir stellen uns als Hintergrundbild auf der Frontpage Hongkong vor. Keine Flash videos oder audio einbindung ! Sprache Englisch, die Texte sollten von uns leicht editierbar sein, falls mal Anpassungen gemacht werden müssen.

```html
<!DOCTYPE html>
<html lang="en">
<head>
<meta charset="utf-8">
<title>Veltrano Group</title>
<link rel="stylesheet" href="https://fonts.googleapis.com/css2?family=Open+Sans:wght@400;600;700&display=swap">
<style>
  :root {
    --header-bg: #141c36;
    --header-line: #4a5a8c;
    --sky-top: #2b3a78;
    --sky-mid: #5467a8;
    --city-glow: #3c3f66;
    --night: #0b0b0d;
    --white: #ffffff;
    --card-bg: #f3f1f2;
    --heading: #111111;
    --text: #3a3a3a;
    --link: #1f3fa8;
    --footer-link: #8a8a8a;
    --footer-copy: #777777;
  }
  * { box-sizing: border-box; margin: 0; padding: 0; }
  html, body { width: 1200px; height: 696px; overflow: hidden; }
  body {
    position: relative;
    background: var(--night);
    font-family: "Open Sans", Arial, sans-serif;
    color: var(--text);
  }
  .backdrop {
    position: absolute; left: 0; top: 0; width: 1200px; height: 696px;
    background: linear-gradient(180deg, var(--sky-top) 0%, var(--sky-mid) 30%, var(--city-glow) 55%, #1a1a24 72%, var(--night) 82%, var(--night) 100%);
  }
  .site-header {
    position: absolute; left: 0; top: 0; width: 1200px; height: 60px;
    background: linear-gradient(180deg, #1b2447 0%, var(--header-bg) 100%);
    border-bottom: 1px solid var(--header-line);
  }
  .welcome {
    position: absolute; left: 198px; top: 17px;
    font-size: 19px; color: var(--white); font-weight: 400;
  }
  .brand {
    position: absolute; right: 198px; top: 9px;
    display: flex; align-items: center; gap: 10px;
    font-size: 31px; font-weight: 700; color: var(--white); letter-spacing: 3px;
  }
  .brand-mark { width: 26px; height: 26px; background: var(--white); }
  .tagline {
    position: absolute; left: 0; top: 76px; width: 1200px; text-align: center;
    font-size: 18px; color: var(--white);
  }
  .card {
    position: absolute; background: var(--card-bg); border-radius: 5px;
    padding: 16px 22px 0 22px;
  }
  .card h2 { font-size: 16px; font-weight: 400; color: var(--heading); margin-bottom: 8px; }
  .card p { font-size: 10.6px; line-height: 18px; margin-bottom: 9px; }
  .card ul { list-style: none; margin-bottom: 4px; }
  .card li { font-size: 10.6px; line-height: 18.8px; position: relative; padding-left: 18px; }
  .card li::before {
    content: ""; position: absolute; left: 4px; top: 6px;
    width: 6px; height: 6px; border-radius: 50%; background: #444;
  }
  .more {
    position: absolute; right: 25px; bottom: 16px;
    font-size: 10.6px; color: var(--link); text-decoration: none;
  }
  .card-opto { left: 197px; top: 119px; width: 394px; height: 157px; }
  .card-agency { left: 197px; top: 290px; width: 394px; height: 121px; }
  .card-consult { left: 197px; top: 424px; width: 394px; height: 202px; }
  .card-finance { left: 609px; top: 119px; width: 393px; height: 157px; }
  .card-trouble { left: 609px; top: 290px; width: 393px; height: 171px; }
  .card-ma { left: 609px; top: 475px; width: 393px; height: 151px; }
  .footer-nav {
    position: absolute; left: 0; top: 641px; width: 1200px;
    display: flex; justify-content: center; gap: 32px; padding-right: 8px;
  }
  .footer-nav a { font-size: 9.5px; color: var(--footer-link); text-decoration: none; }
  .copyright {
    position: absolute; left: 0; top: 661px; width: 1200px; text-align: center;
    font-size: 9.5px; color: var(--footer-copy);
  }
</style>
</head>
<body>
  <div class="backdrop" role="img" aria-label="Night skyline of Hong Kong across the harbour with city lights"></div>

  <header class="site-header">
    <div class="welcome">Welcome to the Veltrano Group...</div>
    <div class="brand"><span class="brand-mark"></span>VELTRANO</div>
  </header>

  <div class="tagline">Our business segments cover quite an area, please select your piont of interest</div>

  <section class="card card-opto">
    <h2>Optoelectronics / Semiconductors</h2>
    <p>We offer an outstanding service to our customers. Based on our 30 years market experience, we have unrivaled skillsets to increase our customers sales volume.</p>
    <p>We differentiate between Consultancy and Agency business models.</p>
  </section>

  <section class="card card-agency">
    <h2>Agency</h2>
    <p>We buy, import and sell optoelectronic semiconductors throughout our salesnetwork, covering Europe and Scandinavia.</p>
    <a class="more" href="#">More...(2)</a>
  </section>

  <section class="card card-consult">
    <h2>Consultancy</h2>
    <p>Consulting means, understanding what the customers want. If you prefer to enter a market silently, we are the right choice.</p>
    <p>This can be:<br>Setup of an european sales network Identifying M&amp;A targets, proxy negotiations Market analysis and recommendations</p>
    <a class="more" href="#">More...(2)</a>
  </section>

  <section class="card card-finance">
    <h2>Technology Financing</h2>
    <ul>
      <li>You or your company have an outstanding product or idea</li>
      <li>For the extension of market shares you need support</li>
      <li>You want to retract from Europe and sell your assets</li>
    </ul>
    <p>This is exactly, what we like and where we can add enormous power.</p>
    <a class="more" href="#">More...(4)</a>
  </section>

  <section class="card card-trouble">
    <h2>Troubleshooting</h2>
    <ul>
      <li>Your project runs out of bounds</li>
      <li>Pricing, quality and milestones are not met by the vendors</li>
      <li>Prototype works but the transition to industrial usage stucks</li>
      <li>You desparately need a second source for mission critical parts</li>
    </ul>
    <p>This is exactly, what we like and where we can add enormous power.</p>
    <a class="more" href="#">More...(5)</a>
  </section>

  <section class="card card-ma">
    <h2>M &amp; A , the silent service</h2>
    <ul>
      <li>You understand the time to market entrance issue</li>
      <li>You want to prove and identify targets for aquisition</li>
      <li>You need a proxy to make first contacts and evaluate</li>
      <li>You just need a concise market overview about your competitors</li>
    </ul>
    <a class="more" href="#">More...(6)</a>
  </section>

  <nav class="footer-nav">
    <a href="#">Home</a>
    <a href="#">Agency</a>
    <a href="#">Consultancy</a>
    <a href="#">Technology Finance</a>
    <a href="#">Troubleshooting</a>
    <a href="#">M&amp;A Silent Service</a>
  </nav>
  <div class="copyright">Copyright 2010. Veltrano Group. All Rights Reserved.</div>
</body>
</html>
```